Glimmerseal pond linings website template

We need a template for our new website. Glimmerseal is currently marketed through www.tarpavale.com.au, and we are moving the pond/dam linings to a dedicated site www.glimmerseal.com.au

The site is essentially brochureware. The content (less landing page & photo gallery) is on the new site to give you a better idea of what we do. We are also on Facebook.com/glimmerseal

We are looking for a template/style which we can adapt to the different sections of the site as required. We also get a lot of phone/tablet visitors so an alternative mobile layout would be a bonus, but by no means required.

I am proficient in HTML/CSS & javascript so can code most designs thrown at me.

Any icons or interface fonts should be freely available web fonts where possible.

Target Market(s)

We are targeting both landscape professionals (design & construction) as well as the DIY market for ponds/wateragrdens.

Industry/Entity Type

Moving

Requirements
Must have
• We need a design (preferably layered PSD or AI) as basis for our overall site look and feel. Fonts/iconography/layout are where we are lacking. We can do the HTML/CSS/JS/PHP internally.
Nice to have
• A style guide either in file or separate would be nice.
Layers with effect (i.e.. :hover, CSS3 transition endpoints, etc)

```html
<!DOCTYPE html>
<html lang="en">
<head>
<meta charset="utf-8">
<title>Glimmerseal – Custom made liners</title>
<link href="https://fonts.googleapis.com/css2?family=PT+Sans:wght@400;700&family=Arimo:wght@400;700&display=swap" rel="stylesheet">
<style>
:root{
  --night:#0f2806;
  --deep:#0c2204;
  --leaf:#3f8a1c;
  --leaf-light:#7cc13a;
  --lime:#c3d52f;
  --moss:#6a9a2a;
  --moss-text:#5f8f25;
  --paper:#f6f6f4;
  --band:#e4e4e0;
  --rule:#d9d9d4;
  --ink:#222;
  --grey:#777;
  --foot:#b9c2b4;
  --white:#fff;
}
*{margin:0;padding:0;box-sizing:border-box}
html,body{width:1009px;height:1200px;overflow:hidden}
body{position:relative;font-family:"Arimo",Arial,sans-serif;background:var(--night);color:var(--ink)}
.leaf-backdrop{position:absolute;left:0;top:109px;width:1009px;height:1091px;
  background:radial-gradient(ellipse at 50% 20%,#7cc440 0%,#3e8f1e 35%,#1c4d0c 70%,var(--night) 100%)}
.masthead{position:absolute;left:0;top:0;width:1009px;height:109px;background:var(--night)}
.brand{position:absolute;left:410px;top:6px;width:168px;height:62px;display:flex;align-items:center;justify-content:center;gap:8px;background:var(--white)}
.brand-mark{width:14px;height:14px;background:var(--lime)}
.brand-name{font-family:"PT Sans",sans-serif;font-weight:700;font-size:20px;color:var(--leaf);letter-spacing:.5px}
.main-nav{position:absolute;top:78px;left:0;width:1009px;display:flex;justify-content:center;gap:24px}
.main-nav a{color:var(--white);font-weight:700;font-size:12.5px;text-decoration:none;letter-spacing:.2px}
.dropdown{position:absolute;left:452px;top:95px;width:126px;height:112px;background:var(--lime);padding:18px 0 0 20px}
.dropdown a{display:block;color:var(--white);font-size:8.5px;font-weight:700;margin-bottom:10px;text-decoration:none}
.hero-title{position:absolute;top:224px;width:1009px;left:10px;text-align:center;color:var(--white);font-size:29px;font-weight:700}
.hero-sub{position:absolute;top:263px;left:388px;width:260px;text-align:center;color:var(--white);font-size:17px;font-weight:700;line-height:21px}
.hero-dots{position:absolute;top:338px;left:479px;display:flex;gap:10px}
.hero-dots span{width:13px;height:13px;border-radius:50%;background:var(--lime)}
.carousel{position:absolute;left:81px;top:382px;width:841px;height:200px;background:var(--deep)}
.carousel-item{position:absolute;top:33px;width:148px;height:136px;background:var(--white);padding:6px}
.carousel-item div{width:100%;height:100%}
.arrow{position:absolute;top:463px;width:39px;height:37px;background:var(--lime)}
.arrow svg{display:block;margin:9px auto}
.features{position:absolute;left:81px;top:598px;width:841px;height:177px;background:var(--paper);display:flex}
.feature{flex:1;border-right:2px solid var(--rule);text-align:center}
.feature:last-child{border-right:0}
.feature h3{height:49px;line-height:49px;background:var(--band);font-family:"PT Sans",sans-serif;font-size:12.5px;color:var(--ink)}
.feature p{margin:12px auto 0;width:140px;font-size:9.5px;color:var(--grey);line-height:16.5px}
.more{display:inline-block;margin-top:14px;width:64px;height:28px;line-height:28px;background:var(--moss);color:var(--white);font-size:10.5px;font-weight:700}
.about{position:absolute;left:81px;top:775px;width:841px;height:221px;background:var(--paper);border-top:2px solid var(--rule)}
.about h2{position:absolute;font-family:"PT Sans",sans-serif;font-size:11.5px;font-weight:700;color:var(--ink)}
.about-photo{position:absolute;left:30px;top:49px;width:240px;height:134px;border:5px solid var(--white);box-shadow:0 0 0 1px var(--rule)}
.about-lead{position:absolute;left:288px;top:50px;width:265px;font-size:10px;font-weight:700;color:var(--moss-text);line-height:15px}
.about-copy{position:absolute;left:288px;top:86px;width:265px;font-size:9.5px;color:var(--grey);line-height:16.5px}
.about-copy b{color:var(--moss-text)}
.service{position:absolute;left:578px;width:250px;height:66px}
.service-photo{position:absolute;left:0;top:0;width:96px;height:66px;border:3px solid var(--white);box-shadow:0 0 0 1px var(--rule)}
.service h4{position:absolute;left:106px;top:0;font-size:10.5px;color:var(--moss-text)}
.service p{position:absolute;left:106px;top:16px;width:140px;font-size:9.5px;color:var(--grey);line-height:15px}
.service a{position:absolute;left:106px;top:52px;font-size:9.5px;color:var(--moss-text);text-decoration:none}
.footer-col{position:absolute;top:1020px}
.footer-col h5{font-family:"PT Sans",sans-serif;font-size:10px;color:var(--white);margin-bottom:13px}
.footer-col li{list-style:none;font-size:9.5px;font-weight:700;color:var(--foot);margin-bottom:5px}
.footer-col.bullets li::before{content:"»";margin-right:10px;color:var(--white)}
.social{position:absolute;top:1027px;left:810px;display:flex;gap:5px}
.social span{width:26px;height:26px;background:var(--moss);border-radius:3px}
.footer-brand{position:absolute;left:733px;top:1066px;width:168px;height:65px;background:var(--white);display:flex;align-items:center;justify-content:center;gap:8px}
.legal{position:absolute;left:115px;top:1157px;font-size:9.5px;color:var(--foot);line-height:13px}
</style>
</head>
<body>
<div class="leaf-backdrop" role="img" aria-label="Close-up photograph of lush green leaves"></div>

<header class="masthead">
  <div class="brand"><span class="brand-mark"></span><span class="brand-name">GLIMMERSEAL</span></div>
  <nav class="main-nav">
    <a href="#">HOME</a><a href="#">ABOUT US</a><a href="#">HAPPENINGS</a><a href="#">GALLERY</a><a href="#">LINER STYLES</a><a href="#">PREPARATION</a><a href="#">INSTALLATION</a><a href="#">CONTACT US</a>
  </nav>
</header>
<div class="dropdown">
  <a href="#">FLAT SHEET LINERS</a><a href="#">COMPOSITE LINERS</a><a href="#">PROFILE LINERS</a><a href="#">PROJECT LINER</a>
</div>

<h1 class="hero-title">WELCOME TO GLIMMERSEAL</h1>
<p class="hero-sub">CUSTOM MADE LINERS FOR PONDS, POOLS AND WATER GARDENS.</p>
<div class="hero-dots"><span></span><span></span><span></span><span></span></div>

<section class="carousel">
  <div class="carousel-item" style="left:31px"><div role="img" aria-label="Shopfront decorated with flowers" style="background:linear-gradient(#7a4a35,#a0422c 60%,#c9a24a)"></div></div>
  <div class="carousel-item" style="left:190px"><div role="img" aria-label="Topiary sculpture on a street" style="background:linear-gradient(#7fa056,#4f7a2a 60%,#686868)"></div></div>
  <div class="carousel-item" style="left:349px"><div role="img" aria-label="Brick shopfront with planters" style="background:linear-gradient(#a4553a,#7d3e2a 60%,#4e4a3e)"></div></div>
  <div class="carousel-item" style="left:507px"><div role="img" aria-label="Window box garden display" style="background:linear-gradient(#caa26a,#5d7a2e 55%,#b04a2e)"></div></div>
  <div class="carousel-item" style="left:665px"><div role="img" aria-label="White shopfront with potted plants" style="background:linear-gradient(#e8e4dc,#b9b4a8 60%,#5e7a3e)"></div></div>
</section>
<div class="arrow" style="left:59px"><svg width="14" height="18" viewBox="0 0 14 18"><path d="M11 2 4 9l7 7" fill="none" stroke="#fff" stroke-width="3"/></svg></div>
<div class="arrow" style="left:904px"><svg width="14" height="18" viewBox="0 0 14 18"><path d="M3 2l7 7-7 7" fill="none" stroke="#fff" stroke-width="3"/></svg></div>

<section class="features">
  <div class="feature"><h3>FLAT SHEET LINERS</h3><p>A flat sheet liner is the most common liner we manufacture and is suitable for most pond designs.</p><span class="more">more</span></div>
  <div class="feature"><h3>COMPOSITE LINERS</h3><p>A flat sheet liner is the most common liner we manufacture and is suitable for most pond designs.</p><span class="more">more</span></div>
  <div class="feature"><h3>PROFILE LINERS</h3><p>A flat sheet liner is the most common liner we manufacture and is suitable for most pond designs.</p><span class="more">more</span></div>
  <div class="feature"><h3>SPECIAL PROJECT LINERS</h3><p>A flat sheet liner is the most common liner we manufacture and is suitable for most pond designs.</p><span class="more">more</span></div>
</section>

<section class="about">
  <h2 style="left:32px;top:22px">WELCOME TO GLIMMERSEALS</h2>
  <div class="about-photo" role="img" aria-label="Garden landscape with tree ferns and a pavilion" style="background:linear-gradient(#b9c8b0,#6f8c4a 55%,#8a5a3a)"></div>
  <p class="about-lead">Mutual understanding with our customers is a pledge of our company's success!</p>
  <p class="about-copy">Glimmerseal has been manufactured, marketed and installed throughout Australia and the Pacific Rim since the early 1980's for a variety of domestic and commercial applications.<br><br>Glimmerseal pond liners put an end to the complicated and time consuming installation used by other <b>Read more...</b></p>
  <h2 style="left:580px;top:26px">OUR SERVICES</h2>
  <div class="service" style="top:48px"><div class="service-photo" role="img" aria-label="Garden pond surrounded by trees" style="background:linear-gradient(#8a9a6a,#4a5e2a 60%,#6a7a5a)"></div><h4>Ordered Nature</h4><p>Praesent vestibulum molestie lacus aenean.</p><a href="#">more info</a></div>
  <div class="service" style="top:128px"><div class="service-photo" role="img" aria-label="Outdoor garden display stand" style="background:linear-gradient(#c6d0d6,#8a9a7a 55%,#7a5a3e)"></div><h4>Outside Verano</h4><p>Praesent vestibulum molestie lacus aenean.</p><a href="#">more info</a></div>
</section>

<footer>
  <div class="footer-col bullets" style="left:113px"><h5>INSTALLATION PROCEDURES</h5><ul><li>Standard Installation</li><li>Folding Corners</li><li>Pipes and Penetrations</li><li>Waterfalls</li><li>Edge finishing</li><li>Water, Plans &amp; Fish</li></ul></div>
  <div class="footer-col" style="left:301px"><h5>RECENT FROM THE BLOG</h5><ul><li>Donec tempor libero</li><li>Vivamus vel sem at</li><li>Etiam commodo convallis</li><li>Etiam dictum egestas</li><li>Phasellus fringilla</li></ul></div>
  <div class="footer-col" style="left:486px"><h5>NAVIGATION</h5><ul><li>Home</li><li>About Us</li><li>Happenings</li><li>Gallery</li><li>Preparation</li><li>Contact Us</li></ul></div>
  <div class="social"><span></span><span></span><span></span></div>
  <div class="footer-brand"><span class="brand-mark"></span><span class="brand-name">GLIMMERSEAL</span></div>
  <p class="legal">COPYRIGHT 2013. ALL RIGHTS RESERVED.<br>TERMS &amp; CONDITIONS &nbsp;- &nbsp;PRIVACY &nbsp;- &nbsp;DISCLAIMER</p>
</footer>
</body>
</html>
```